Copper Ridge Business Cards For New Startup

I am looking for you to design some business cards for a new startup https://copperridgehub.example. I have supplied logo, brand guidelines and our signatures as a guide.

We need this to reflect the brand guidelines and the website for brand consistency,

What is Copper Ridge?

Mallorca's Business Growth Community
Join your new business community full of passionate entrepreneurs who
love to solve problems and help each other grow together!

Any questions you can ask.

Target Market(s)

Business to Business

Contact Information for Business Card

These are attached (signatures) to the job

Font styles to use
Other font styles liked:
• Open Sans

Requirements
Must have
• Match design guidelines
Nice to have
• Photos of our faces so people remember us

```html
<!DOCTYPE html>
<html lang="en">
<head>
<meta charset="utf-8">
<title>Copper Ridge – Business Card</title>
<link href="https://fonts.googleapis.com/css2?family=Montserrat:wght@300;400;600;700&display=swap" rel="stylesheet">
<style>
  :root {
    --page-bg: #e6e9ed;
    --card-bg-top: #f4f6f8;
    --card-bg-bottom: #e3e9ef;
    --olive-dark: #3f3d1c;
    --olive-ink: #4a4822;
    --text-ink: #3a3826;
    --band-bg: rgba(56, 54, 24, 0.9);
    --band-ring: #d9d6c4;
    --photo-top: #c9d5e0;
    --photo-mid: #a4a9ad;
    --photo-bottom: #2e3442;
  }
  html, body {
    margin: 0;
    padding: 0;
    width: 1200px;
    height: 900px;
    overflow: hidden;
    background: var(--page-bg);
  }
  .business-card {
    position: absolute;
    left: 120px;
    top: 178px;
    width: 960px;
    height: 544px;
    background: linear-gradient(180deg, var(--card-bg-top), var(--card-bg-bottom));
    box-shadow: 0 10px 30px rgba(0,0,0,0.12);
    overflow: hidden;
    font-family: "Montserrat", Arial, sans-serif;
    color: var(--text-ink);
  }
  .portrait {
    position: absolute;
    left: 0;
    top: 0;
    width: 474px;
    height: 544px;
    background: linear-gradient(180deg, var(--photo-top) 0%, var(--photo-mid) 55%, var(--photo-bottom) 100%);
  }
  .divider {
    position: absolute;
    left: 480px;
    top: 100px;
    width: 3px;
    height: 310px;
    background: var(--olive-dark);
  }
  .brand {
    position: absolute;
    left: 510px;
    top: 100px;
    display: flex;
    align-items: center;
    gap: 18px;
  }
  .brand-mark {
    width: 80px;
    height: 80px;
    border: 3px solid var(--olive-ink);
    border-radius: 50%;
    box-sizing: border-box;
  }
  .brand-name {
    font-size: 38px;
    font-weight: 600;
    letter-spacing: 0.5px;
    color: var(--olive-ink);
    text-transform: uppercase;
  }
  .person-name {
    position: absolute;
    left: 508px;
    top: 212px;
    margin: 0;
    font-size: 36px;
    letter-spacing: 0.5px;
    color: var(--olive-ink);
    text-transform: uppercase;
    line-height: 1;
  }
  .person-name .first { font-weight: 700; }
  .person-name .last { font-weight: 300; }
  .person-role {
    position: absolute;
    left: 508px;
    top: 256px;
    margin: 0;
    font-size: 24px;
    font-weight: 400;
    line-height: 1;
  }
  .contact-list {
    position: absolute;
    left: 516px;
    top: 304px;
    margin: 0;
    padding: 0;
    list-style: none;
  }
  .contact-list li {
    display: flex;
    align-items: center;
    height: 35px;
    font-size: 26px;
    font-weight: 400;
  }
  .contact-list svg {
    width: 24px;
    height: 24px;
    margin-right: 16px;
    flex: none;
    fill: var(--olive-dark);
  }
  .social-band {
    position: absolute;
    left: 489px;
    top: 485px;
    width: 471px;
    height: 59px;
    background: var(--band-bg);
  }
  .social-ring {
    position: absolute;
    top: 10px;
    width: 40px;
    height: 40px;
    border: 2px solid var(--band-ring);
    border-radius: 50%;
    box-sizing: border-box;
  }
</style>
</head>
<body>
  <div class="business-card">
    <div class="portrait" role="img" aria-label="Portrait photo of the founder in a dark blazer"></div>
    <div class="divider"></div>

    <div class="brand">
      <div class="brand-mark"></div>
      <span class="brand-name">Copper Ridge</span>
    </div>

    <h1 class="person-name"><span class="first">Daniel</span> <span class="last">Moreau</span></h1>
    <p class="person-role">Founder &amp; Growth Hacker | Copper</p>

    <ul class="contact-list">
      <li>
        <svg viewBox="0 0 24 24" aria-hidden="true"><path d="M6.6 10.8a15.1 15.1 0 0 0 6.6 6.6l2.2-2.2c.3-.3.7-.4 1-.2 1.1.4 2.3.6 3.6.6.6 0 1 .4 1 1V20c0 .6-.4 1-1 1C10.6 21 3 13.4 3 4c0-.6.4-1 1-1h3.5c.6 0 1 .4 1 1 0 1.3.2 2.5.6 3.6.1.3 0 .7-.2 1z"/></svg>
        +34 611 482 905
      </li>
      <li>
        <svg viewBox="0 0 24 24" aria-hidden="true"><path d="M2 5h20v14H2z M3.5 6.5 12 13l8.5-6.5" fill="none" stroke="currentColor"/><path d="M2 5h20v14H2zM4 7v10h16V7l-8 6z"/></svg>
        dm@copperridgehub.example
      </li>
      <li>
        <svg viewBox="0 0 24 24" aria-hidden="true"><circle cx="12" cy="12" r="10"/><path d="M2 12h20M12 2c3 3 3 17 0 20M12 2c-3 3-3 17 0 20" stroke="#e9eef2" stroke-width="1.5" fill="none"/></svg>
        copperridgehub.example
      </li>
    </ul>

    <div class="social-band">
      <span class="social-ring" style="left:26px"></span>
      <span class="social-ring" style="left:89px"></span>
      <span class="social-ring" style="left:153px"></span>
      <span class="social-ring" style="left:215px"></span>
      <span class="social-ring" style="left:278px"></span>
    </div>
  </div>
</body>
</html>
```